Brightmoor Capital
"The Business and Corporate Finance Specialists, Mortgages and Remortgages"
Professional
Dorian Kellaway
Director
14 Quillfield Parade
Harrow
London
HA7 2QX
Dorian@brightmoorcapital.example
www.brightmoorcapital.example
Letterhead and compliment slips require the following regulatory text:
"Registered in England and Wales number: 08213947
Brightmoor Capital Ltd is authorised and regulated by the Monetary Oversight Council for regulated mortgage contracts and non-investment insurance activities."
Be creative - open to suggestions

```html
<!DOCTYPE html>
<html lang="en">
<head>
<meta charset="utf-8">
<title>Brightmoor Capital – Stationery</title>
<link href="https://fonts.googleapis.com/css2?family=Open+Sans:wght@400;600;700&family=Great+Vibes&display=swap" rel="stylesheet">
<style>
  :root{
    --bg:#e8e5e0;
    --paper:#ffffff;
    --ink:#3a3a3a;
    --muted:#7a7a7a;
    --orange:#f0821e;
    --amber:#f7b51c;
    --green:#8cc63f;
    --green-dark:#5f9a22;
    --charcoal:#1c1c1c;
    --shadow:0 2px 6px rgba(0,0,0,.25);
  }
  *{box-sizing:border-box;margin:0;padding:0}
  html,body{width:1200px;height:374px;overflow:hidden}
  body{background:var(--bg);font-family:"Open Sans",Arial,sans-serif;color:var(--ink);position:relative}
  .sheet{position:absolute;background:var(--paper);box-shadow:var(--shadow);overflow:hidden}
  .brand{font-weight:600;color:var(--orange);white-space:nowrap;display:flex;align-items:center;gap:3px;line-height:1}
  .brand .dot{display:inline-block;border-radius:50%;background:var(--green)}
  .tagline{color:var(--muted);line-height:1.25}
  .band{position:absolute;left:0;top:0;bottom:0;background:linear-gradient(180deg,var(--amber),var(--orange))}
  .small{font-size:3.6px;line-height:1.45;color:var(--muted)}

  /* business cards */
  .card{width:110px;height:68px}
  .card--dark{background:var(--charcoal)}
  .card--dark .brand{color:var(--amber)}
  .card--dark .small{color:#cfcfcf}
  .card .brand{position:absolute;left:7px;top:9px;font-size:8px}
  .card .brand .dot{width:5px;height:5px}
  .card .tagline{position:absolute;left:7px;top:20px;font-size:3.3px;width:96px}
  .card .contact{position:absolute;left:7px;bottom:7px}
  .card .web{position:absolute;right:7px;bottom:7px;text-align:right}
  .card .stripe{position:absolute;left:0;right:0;bottom:0;height:3px;background:linear-gradient(90deg,var(--amber),var(--orange))}
  .card .center{position:absolute;inset:0;display:flex;align-items:center;justify-content:center}
  .card .center .brand{position:static;font-size:10px}

  /* letterhead */
  .letterhead{left:322px;top:26px;width:168px;height:324px}
  .letterhead .band{width:9px}
  .letterhead .brand{position:absolute;left:18px;top:14px;font-size:11px}
  .letterhead .brand .dot{width:7px;height:7px}
  .letterhead .tagline{position:absolute;left:18px;top:28px;font-size:3.8px;width:80px}
  .letterhead .address{position:absolute;right:8px;top:12px;text-align:right}
  .letterhead .legal{position:absolute;left:18px;right:8px;bottom:10px;border-top:.6px solid var(--orange);padding-top:3px;font-size:3.2px}

  /* compliment slip */
  .slip{left:505px;top:26px;width:255px;height:132px}
  .slip .band{width:9px}
  .slip .brand{position:absolute;left:18px;top:12px;font-size:11px}
  .slip .brand .dot{width:7px;height:7px}
  .slip .tagline{position:absolute;left:18px;top:26px;font-size:3.8px;width:90px}
  .slip .address{position:absolute;right:10px;top:10px;text-align:right}
  .slip .greeting{position:absolute;left:60px;top:52px;font-family:"Great Vibes",cursive;font-size:23px;color:#222}
  .slip .legal{position:absolute;left:18px;right:10px;bottom:7px;border-top:.6px solid var(--orange);padding-top:2px;font-size:3.1px}

  /* continuation sheet */
  .continuation{left:590px;top:196px;width:170px;height:152px}
  .continuation .band{width:9px}
  .continuation .brand{position:absolute;left:18px;top:12px;font-size:10px}
  .continuation .brand .dot{width:6px;height:6px}
  .continuation .address{position:absolute;right:8px;top:10px;text-align:right}
  .continuation .legal{position:absolute;left:18px;right:8px;bottom:7px;border-top:.6px solid var(--orange);padding-top:2px;font-size:3px}

  /* envelopes */
  .envelope{width:380px;height:96px}
  .envelope .flap{position:absolute;left:0;top:0;width:100%;height:100%}
  .envelope .brand{position:absolute;left:50%;top:46px;transform:translateX(-50%);font-size:9px}
  .envelope .brand .dot{width:6px;height:6px}
  .envelope--green{left:790px;top:18px}
  .envelope--green .brand{color:var(--paper)}
  .envelope--green .brand .dot{background:var(--amber)}
  .envelope--dark{left:800px;top:132px;background:var(--charcoal)}
  .envelope--dark .brand{color:var(--amber)}
  .envelope--white{left:810px;top:246px;height:108px}
  .envelope .wave{position:absolute;left:0;right:0;top:0;height:100%}
</style>
</head>
<body>

<!-- business cards -->
<div class="sheet card card--dark" style="left:20px;top:178px">
  <div class="brand"><span class="dot"></span>Brightmoor Capital</div>
  <div class="tagline">The Business and Corporate Finance Specialists, Mortgages and Remortgages</div>
  <div class="contact small">Dorian Kellaway · Director<br>14 Quillfield Parade, Harrow<br>London HA7 2QX</div>
  <div class="stripe"></div>
</div>
<div class="sheet card" style="left:140px;top:178px">
  <div class="brand"><span class="dot"></span>Brightmoor Capital</div>
  <div class="tagline">The Business and Corporate Finance Specialists, Mortgages and Remortgages</div>
  <div class="contact small">Dorian Kellaway · Director<br>Dorian@brightmoorcapital.example</div>
  <div class="stripe"></div>
</div>
<div class="sheet card" style="left:20px;top:272px">
  <div class="center"><div class="brand"><span class="dot"></span>Brightmoor Capital</div></div>
  <div class="web small" style="left:7px;text-align:center">www.brightmoorcapital.example</div>
  <div class="stripe"></div>
</div>
<div class="sheet card card--dark" style="left:140px;top:272px">
  <div class="center"><div class="brand"><span class="dot"></span>Brightmoor Capital</div></div>
  <div class="stripe"></div>
</div>

<!-- letterhead -->
<div class="sheet letterhead">
  <div class="band"></div>
  <div class="brand"><span class="dot"></span>Brightmoor Capital</div>
  <div class="tagline">The Business and Corporate Finance Specialists, Mortgages and Remortgages</div>
  <div class="address small">14 Quillfield Parade<br>Harrow<br>London<br>HA7 2QX<br>Dorian@brightmoorcapital.example<br>www.brightmoorcapital.example</div>
  <div class="legal small">Registered in England and Wales number: 08213947<br>Brightmoor Capital Ltd is authorised and regulated by the Monetary Oversight Council for regulated mortgage contracts and non-investment insurance activities.</div>
</div>

<!-- compliment slip -->
<div class="sheet slip">
  <div class="band"></div>
  <div class="brand"><span class="dot"></span>Brightmoor Capital</div>
  <div class="tagline">The Business and Corporate Finance Specialists, Mortgages and Remortgages</div>
  <div class="address small">14 Quillfield Parade, Harrow<br>London HA7 2QX<br>Dorian@brightmoorcapital.example<br>www.brightmoorcapital.example</div>
  <div class="greeting">With Compliments</div>
  <div class="legal small">Registered in England and Wales number: 08213947 · Brightmoor Capital Ltd is authorised and regulated by the Monetary Oversight Council for regulated mortgage contracts and non-investment insurance activities.</div>
</div>

<!-- continuation sheet -->
<div class="sheet continuation">
  <div class="band"></div>
  <div class="brand"><span class="dot"></span>Brightmoor Capital</div>
  <div class="address small">14 Quillfield Parade<br>Harrow, London<br>HA7 2QX</div>
  <div class="legal small">Registered in England and Wales number: 08213947</div>
</div>

<!-- envelopes -->
<div class="sheet envelope envelope--green">
  <svg class="wave" viewBox="0 0 380 96" preserveAspectRatio="none">
    <defs>
      <linearGradient id="greenFill" x1="0" y1="0" x2="0" y2="1">
        <stop offset="0" stop-color="#a6d356"/><stop offset="1" stop-color="#5f9a22"/>
      </linearGradient>
    </defs>
    <path d="M0 0H380V58C300 40 230 92 150 82C90 74 40 50 0 62Z" fill="url(#greenFill)"/>
  </svg>
  <svg class="flap" viewBox="0 0 380 96" preserveAspectRatio="none">
    <path d="M0 0L190 44L380 0" fill="none" stroke="rgba(0,0,0,.15)" stroke-width="1"/>
  </svg>
  <div class="brand" style="top:24px"><span class="dot"></span>Brightmoor Capital</div>
</div>
<div class="sheet envelope envelope--dark">
  <svg class="flap" viewBox="0 0 380 96" preserveAspectRatio="none">
    <path d="M0 0L190 44L380 0" fill="#2a2a2a" stroke="rgba(255,255,255,.12)" stroke-width="1"/>
  </svg>
  <div class="brand"><span class="dot"></span>Brightmoor Capital</div>
</div>
<div class="sheet envelope envelope--white">
  <svg class="flap" viewBox="0 0 380 108" preserveAspectRatio="none">
    <path d="M0 0L190 50L380 0" fill="#f4f4f4" stroke="rgba(0,0,0,.12)" stroke-width="1"/>
    <path d="M0 108L190 58L380 108" fill="none" stroke="rgba(0,0,0,.08)" stroke-width="1"/>
  </svg>
  <div class="brand" style="top:30px"><span class="dot"></span>Brightmoor Capital</div>
</div>

</body>
</html>
```